KT Appraisals BV business cards (a financial services company)

I am looking for a business card design that stands out in the financial advisory field of business & intellectual property valuation. The business card design should be conservative, yet different. Address details have changed since the attached business card. New address is:

Dorpelstraat 27
4817 KM Leiden
The Netherlands

Telephone number remains the same.

```html
<!DOCTYPE html>
<html lang="en">
<head>
<meta charset="utf-8">
<title>KT Appraisals BV – Business Cards</title>
<link href="https://fonts.googleapis.com/css2?family=Montserrat:wght@300;400;700&display=swap" rel="stylesheet">
<style>
  :root {
    --bg: #1c1c1c;
    --card: #2a2626;
    --ink: #ffffff;
    --ink-soft: #d9d9d9;
  }
  * { box-sizing: border-box; margin: 0; padding: 0; }
  html, body {
    width: 1200px; height: 900px; overflow: hidden;
    background: var(--bg);
    font-family: "Montserrat", sans-serif;
    color: var(--ink);
  }
  .stage { position: relative; width: 1200px; height: 900px; }

  .card {
    position: absolute;
    width: 540px; height: 310px;
    background: var(--card);
    box-shadow: 0 18px 40px rgba(0,0,0,.55);
  }

  .brand {
    display: flex; align-items: center; gap: 10px;
    font-weight: 300; text-transform: uppercase; letter-spacing: .08em;
    color: var(--ink); white-space: nowrap;
  }
  .brand-square { border: 1.5px solid var(--ink); flex: none; }

  /* Details side */
  .card-details { left: 70px; top: 130px; }
  .card-details .brand { position: absolute; left: 90px; top: 62px; font-size: 22px; }
  .card-details .brand-square { width: 16px; height: 16px; }

  .person { position: absolute; right: 34px; top: 112px; text-align: right; }
  .person-name { font-size: 17px; font-weight: 400; }
  .person-name strong { font-weight: 700; }
  .person-creds { font-size: 9px; font-weight: 300; margin-left: 4px; }
  .person-role { font-size: 10px; font-weight: 300; color: var(--ink-soft); margin-top: 2px; }
  .person-rule { height: 1.5px; background: var(--ink); width: 230px; margin: 8px 0 10px auto; }
  .address { font-size: 11px; font-weight: 700; line-height: 1.75; }

  .contact-rule { position: absolute; left: 28px; right: 34px; top: 228px; height: 1.5px; background: var(--ink); }
  .contact { position: absolute; left: 28px; top: 240px; font-size: 11px; font-weight: 300; line-height: 1.9; }
  .contact li { list-style: none; display: flex; align-items: center; gap: 7px; }
  .contact svg { width: 11px; height: 11px; fill: var(--ink); }

  /* Logo side */
  .card-logo { left: 590px; top: 450px; }
  .frame { position: absolute; inset: 14px; border: 1.5px solid var(--ink); border-bottom: none; }
  .frame-foot { position: absolute; left: 14px; right: 14px; bottom: 14px; display: flex; align-items: center; gap: 14px; }
  .frame-foot::before, .frame-foot::after { content: ""; flex: 1; height: 1.5px; background: var(--ink); }
  .web { font-size: 12px; font-weight: 300; letter-spacing: .28em; }
  .card-logo .brand { position: absolute; left: 50%; top: 50%; transform: translate(-50%, -62%); font-size: 30px; gap: 14px; }
  .card-logo .brand-square { width: 22px; height: 22px; }
</style>
</head>
<body>
<main class="stage">

  <section class="card card-details" aria-label="Card back with contact details">
    <div class="brand"><span class="brand-square"></span><span class="brand-name">KT Appraisals</span></div>

    <div class="person">
      <p class="person-name">Martin <strong>Hale</strong><span class="person-creds">CFA, ASA, RV</span></p>
      <p class="person-role">Managing Director</p>
      <div class="person-rule"></div>
      <p class="address">Dorpelstraat 27<br>4817 KM Leiden The Netherlands</p>
    </div>

    <div class="contact-rule"></div>
    <ul class="contact">
      <li>
        <svg viewBox="0 0 24 24" aria-hidden="true"><path d="M6.6 10.8a15.2 15.2 0 0 0 6.6 6.6l2.2-2.2c.3-.3.7-.4 1-.2 1.1.4 2.3.6 3.6.6.6 0 1 .4 1 1V20c0 .6-.4 1-1 1A17 17 0 0 1 3 4c0-.6.4-1 1-1h3.5c.6 0 1 .4 1 1 0 1.3.2 2.5.6 3.6.1.3 0 .7-.2 1z"/></svg>
        +31 (0)70 384 1127
      </li>
      <li>
        <svg viewBox="0 0 24 24" aria-hidden="true"><path d="M2 5h20v14H2z M3.5 6.5 12 13l8.5-6.5v11h-17z" fill-rule="evenodd"/></svg>
        mhale@ktappraisals.com
      </li>
    </ul>
  </section>

  <section class="card card-logo" aria-label="Card front with company name">
    <div class="frame"></div>
    <div class="brand"><span class="brand-square"></span><span class="brand-name">KT Appraisals</span></div>
    <div class="frame-foot"><span class="web">www.ktappraisals.com</span></div>
  </section>

</main>
</body>
</html>
```